Manufacturing company needs new business card.

I need a unique Business Card that will truly stand out. Nothing too busy. Simple is good, right? Not looking for a standard design either. No cookie cutter layout. I am just looking for something interesting and a bit different. Does't have to completely off the wall crazy, just not your run of the mill business card. Clean and modern with a touch of industrial.

Target Market(s)

Air conditioning industry, Architects, builders.

Industry/Entity Type

Business

Contact Information for Business Card

Details to be included on card are:

Peter Vance
Managing Director

T: 1300 847 519
M: 0428 593 174
W: www.brenvaleworks.com.au
E: peter.vance@brenvaleworks.com.au
A: 58 Harwick Lane, Sydney NSW 2000

Font styles to use
Sans Serif

Colors
0355a3
848484
fbfbfb

Requirements
Must have
• Card design must be landscape.

```html
<!DOCTYPE html>
<html lang="en">
<head>
<meta charset="utf-8">
<title>Brenvale Works – Business Card</title>
<link rel="stylesheet" href="https://fonts.googleapis.com/css2?family=Oswald:wght@500;600&family=Open+Sans:wght@400;600&display=swap">
<style>
  :root {
    --stage: #7f9abf;
    --card-grey: #7b7c7e;
    --card-light: #8a8b8d;
    --card-dark: #707173;
    --panel: rgba(0, 0, 0, 0.07);
    --brand-blue: #0355a3;
    --badge-blue: #3a73bd;
    --ink-light: #fbfbfb;
  }
  * { box-sizing: border-box; margin: 0; padding: 0; }
  html, body {
    width: 1200px;
    height: 1000px;
    overflow: hidden;
    background: var(--stage);
  }
  .stage {
    position: relative;
    width: 1200px;
    height: 1000px;
    display: flex;
    flex-direction: column;
    align-items: center;
    justify-content: center;
    gap: 60px;
  }
  .card {
    position: relative;
    width: 760px;
    height: 420px;
    overflow: hidden;
    border-radius: 3px;
    background:
      linear-gradient(115deg,
        var(--card-dark) 0%, var(--card-dark) 18%,
        var(--card-grey) 18%, var(--card-grey) 34%,
        var(--card-light) 34%, var(--card-light) 52%,
        var(--card-grey) 52%, var(--card-grey) 72%,
        var(--card-dark) 72%, var(--card-dark) 100%);
    box-shadow: 0 14px 30px rgba(20, 30, 60, 0.28);
  }

  /* Front: company name */
  .brand {
    position: absolute;
    left: 0; right: 0; top: 0; bottom: 0;
    display: flex;
    align-items: center;
    justify-content: center;
    gap: 18px;
  }
  .brand-mark {
    width: 34px;
    height: 34px;
    background: var(--ink-light);
  }
  .brand-name {
    font-family: "Open Sans", sans-serif;
    font-weight: 600;
    font-size: 34px;
    letter-spacing: 0.5px;
    color: var(--ink-light);
  }

  /* Back: contact details */
  .person {
    position: absolute;
    left: 58px;
    top: 62px;
  }
  .person-name {
    font-family: "Oswald", sans-serif;
    font-weight: 600;
    font-size: 46px;
    line-height: 1;
    letter-spacing: 1px;
    text-transform: uppercase;
    color: var(--brand-blue);
  }
  .person-role {
    margin-top: 6px;
    font-family: "Oswald", sans-serif;
    font-weight: 500;
    font-size: 17px;
    letter-spacing: 1px;
    text-transform: uppercase;
    color: var(--ink-light);
  }
  .contact-panel {
    position: absolute;
    left: 240px;
    top: 170px;
    width: 470px;
    height: 200px;
    background: var(--panel);
    padding: 26px 28px;
  }
  .contact-list { list-style: none; }
  .contact-item {
    display: flex;
    align-items: center;
    gap: 12px;
    height: 30px;
    font-family: "Open Sans", sans-serif;
    font-size: 16px;
    color: var(--ink-light);
  }
  .contact-badge {
    width: 20px;
    height: 20px;
    background: var(--badge-blue);
    color: var(--ink-light);
    font-family: "Open Sans", sans-serif;
    font-weight: 600;
    font-size: 12px;
    display: flex;
    align-items: center;
    justify-content: center;
  }
</style>
</head>
<body>
  <main class="stage">
    <section class="card card-front" aria-label="Card front">
      <div class="brand">
        <span class="brand-mark"></span>
        <span class="brand-name">Brenvale Works Australia</span>
      </div>
    </section>

    <section class="card card-back" aria-label="Card back">
      <div class="person">
        <h1 class="person-name">Peter Vance</h1>
        <p class="person-role">Managing Director</p>
      </div>
      <div class="contact-panel">
        <ul class="contact-list">
          <li class="contact-item"><span class="contact-badge">T</span>1300 847 519</li>
          <li class="contact-item"><span class="contact-badge">M</span>0428 593 174</li>
          <li class="contact-item"><span class="contact-badge">W</span>www.brenvaleworks.com.au</li>
          <li class="contact-item"><span class="contact-badge">E</span>peter.vance@brenvaleworks.com.au</li>
          <li class="contact-item"><span class="contact-badge">A</span>58 Harwick Lane, Sydney NSW 2000</li>
        </ul>
      </div>
    </section>
  </main>
</body>
</html>
```